Fixed price car insurance banner ad for insurance broker

We need a banner ad for addition to web pages and which will advertise an innovative insurance product we are selling.

We are an insurance broker and our product is a fixed price car insurance product.

The banner ad needs to display the company logo. This will be uploaded within the file upload section.

The remainder of the banner ad needs to explain what we are offering and also include the gear stick picture for impact.

We would like to see colours that tie in with the corporate colours, or alternative are striking and have presence on even the busiest web page I.e. Black banner and silver / white text. Please see the file upload for a sample of the brochure we are preparing for this product.

Target Market(s)

Private and commercial clients with both regular and high value motor vehicles.

Industry/Entity Type

Car Insurance

Font styles to use
Serif
Sans Serif

Colors

Designer to choose colors to be used in the design.

Requirements
Must have
• The banner must have the company logo on both pages.

I would like the advert to scroll / roll / fade or other between two pages displaying the following text:

Page 1
"Motor Insurance Scheme"
"Anything But Standard"
and including the gear knob picture

Page 2
Any Driver, Any Car, No Forms and One Flat Premium*

On clicking the banner ad, this will open an email, pre populated with email contact to request more detail.

Nice to have
• Open to your suggestions on this
Should not have
• Nothing at this stage. I will guide you when the ads are being submitted.

```html
<!DOCTYPE html>
<html lang="en">
<head>
<meta charset="utf-8">
<title>Halden Insurance – Banner Set</title>
<link rel="stylesheet" href="https://fonts.googleapis.com/css2?family=Oxygen:wght@300;400&family=Share+Tech+Mono&display=swap">
<style>
  :root {
    --page: #ffffff;
    --frame: #8a8a8a;
    --navy-deep: #0a1230;
    --navy: #142a52;
    --teal: #0e3a50;
    --chevron: #0c1a44;
    --logo-ink: #1f2f8a;
    --cream: #f2e8d2;
    --white: #ffffff;
    --premium-red: #e8141c;
    --cta-orange: #f7941d;
    --cta-grey: #d8d8d8;
    --label-ink: #111111;
  }
  html, body {
    margin: 0;
    padding: 0;
    width: 1200px;
    height: 900px;
    overflow: hidden;
    background: var(--page);
  }
  .sheet {
    position: relative;
    width: 1200px;
    height: 900px;
  }
  .size-label {
    position: absolute;
    margin: 0;
    font-family: "Share Tech Mono", monospace;
    font-size: 24px;
    font-weight: 400;
    color: var(--label-ink);
  }
  .size-label--leaderboard { left: 30px; top: 50px; }
  .size-label--full { left: 302px; top: 600px; }
  .banner {
    position: absolute;
    display: block;
  }
  .banner--leaderboard { left: 20px; width: 1157px; height: 145px; }
  .banner--full { left: 302px; width: 595px; height: 75px; }
  .banner text { font-family: "Oxygen", sans-serif; }
  .logo-name { fill: var(--logo-ink); font-size: 46px; font-weight: 400; }
  .headline { fill: var(--cream); font-size: 46px; font-weight: 400; }
  .strapline { fill: var(--white); font-size: 24px; letter-spacing: 1.5px; }
  .info { fill: var(--white); font-size: 19px; }
  .cta { fill: var(--cta-orange); font-size: 24px; }
  .offer { fill: var(--white); font-size: 30px; }
  .premium { fill: var(--premium-red); font-size: 42px; }
  .learn { fill: var(--cta-grey); font-size: 24px; font-weight: 300; }
  .learn .cta-link { fill: var(--cta-orange); }
  .frame { fill: none; stroke: var(--frame); stroke-width: 1.5; }
</style>
</head>
<body>
<main class="sheet">

  <svg width="0" height="0" aria-hidden="true" style="position:absolute">
    <defs>
      <linearGradient id="night-band" x1="0" y1="0" x2="1" y2="0">
        <stop offset="0" stop-color="#0e2a4a"/>
        <stop offset="0.55" stop-color="#080c22"/>
        <stop offset="1" stop-color="#1b2f58"/>
      </linearGradient>
      <radialGradient id="knob-tone" cx="0.45" cy="0.4" r="0.6">
        <stop offset="0" stop-color="#f4f4f4"/>
        <stop offset="0.55" stop-color="#b9bcc0"/>
        <stop offset="0.8" stop-color="#4a4d52"/>
        <stop offset="1" stop-color="#111111"/>
      </radialGradient>
    </defs>
  </svg>

  <p class="size-label size-label--leaderboard">728 x90</p>

  <!-- Leaderboard, page 1 -->
  <svg class="banner banner--leaderboard" style="top:105px" viewBox="0 0 1157 145" preserveAspectRatio="none">
    <rect width="1157" height="145" fill="url(#night-band)"/>
    <polygon points="0,0 355,0 285,72 430,145 0,145" fill="var(--white)"/>
    <polygon points="355,0 520,0 450,72 540,145 430,145 285,72" fill="var(--teal)"/>
    <polygon points="520,0 600,0 530,72 620,145 540,145 450,72" fill="var(--chevron)"/>
    <text class="logo-name" x="30" y="62">Halden</text>
    <text class="logo-name" x="30" y="118">Insurance</text>
    <text class="headline" x="362" y="56">Motor Insurance Scheme</text>
    <text class="strapline" x="958" y="92" text-anchor="end">ANYTHING BUT STANDARD</text>
    <text class="info" x="558" y="132">To Get More Information</text>
    <text class="cta" x="958" y="132" text-anchor="end">CLICK HERE !</text>
    <circle cx="1090" cy="72" r="72" fill="url(#knob-tone)" role="img" aria-label="Photo of a chrome gear knob with shift pattern"/>
    <rect class="frame" x="0.75" y="0.75" width="1155.5" height="143.5"/>
  </svg>

  <!-- Leaderboard, page 2 -->
  <svg class="banner banner--leaderboard" style="top:256px" viewBox="0 0 1157 145" preserveAspectRatio="none">
    <rect width="1157" height="145" fill="url(#night-band)"/>
    <polygon points="0,0 355,0 285,72 430,145 0,145" fill="var(--white)"/>
    <polygon points="355,0 520,0 450,72 540,145 430,145 285,72" fill="var(--teal)"/>
    <polygon points="520,0 600,0 530,72 620,145 540,145 450,72" fill="var(--chevron)"/>
    <text class="logo-name" x="30" y="62">Halden</text>
    <text class="logo-name" x="30" y="118">Insurance</text>
    <text class="offer" x="350" y="38">Any Driver,</text>
    <text class="offer" x="430" y="82">Any Car,</text>
    <text class="offer" x="508" y="128">No Forms</text>
    <text class="premium" x="588" y="80">&amp; One Flat Premium*</text>
    <text class="learn" x="753" y="130"><tspan class="cta-link">Click Here</tspan> to Learn More</text>
    <circle cx="1095" cy="58" r="72" fill="url(#knob-tone)" role="img" aria-label="Photo of a chrome gear knob with shift pattern"/>
    <rect class="frame" x="0.75" y="0.75" width="1155.5" height="143.5"/>
  </svg>

  <!-- Leaderboard, page 2 mirrored -->
  <svg class="banner banner--leaderboard" style="top:408px" viewBox="0 0 1157 145" preserveAspectRatio="none">
    <rect width="1157" height="145" fill="url(#night-band)"/>
    <polygon points="1157,0 822,0 892,72 757,145 1157,145" fill="var(--white)"/>
    <polygon points="822,0 667,0 737,72 647,145 757,145 892,72" fill="var(--teal)"/>
    <polygon points="667,0 587,0 657,72 567,145 647,145 737,72" fill="var(--chevron)"/>
    <text class="logo-name" x="895" y="62">Halden</text>
    <text class="logo-name" x="895" y="118">Insurance</text>
    <circle cx="68" cy="72" r="72" fill="url(#knob-tone)" role="img" aria-label="Photo of a chrome gear knob with shift pattern"/>
    <text class="offer" x="155" y="38">Any Driver,</text>
    <text class="offer" x="233" y="82">Any Car,</text>
    <text class="offer" x="312" y="128">No Forms</text>
    <text class="premium" x="412" y="68">&amp; One Flat Premium*</text>
    <text class="learn" x="552" y="128"><tspan class="cta-link">Click Here</tspan> to Learn More</text>
    <rect class="frame" x="0.75" y="0.75" width="1155.5" height="143.5"/>
  </svg>

  <p class="size-label size-label--full">468 x60</p>

  <!-- Full banner, page 1 -->
  <svg class="banner banner--full" style="top:642px" viewBox="0 0 1157 145" preserveAspectRatio="none">
    <rect width="1157" height="145" fill="url(#night-band)"/>
    <polygon points="0,0 355,0 285,72 430,145 0,145" fill="var(--white)"/>
    <polygon points="355,0 520,0 450,72 540,145 430,145 285,72" fill="var(--teal)"/>
    <polygon points="520,0 600,0 530,72 620,145 540,145 450,72" fill="var(--chevron)"/>
    <text class="logo-name" x="30" y="62">Halden</text>
    <text class="logo-name" x="30" y="118">Insurance</text>
    <text class="headline" x="362" y="56">Motor Insurance Scheme</text>
    <text class="strapline" x="958" y="92" text-anchor="end">ANYTHING BUT STANDARD</text>
    <text class="info" x="558" y="132">To Get More Information</text>
    <text class="cta" x="958" y="132" text-anchor="end">CLICK HERE !</text>
    <circle cx="1090" cy="72" r="72" fill="url(#knob-tone)" role="img" aria-label="Photo of a chrome gear knob with shift pattern"/>
    <rect class="frame" x="1.5" y="1.5" width="1154" height="142"/>
  </svg>

  <!-- Full banner, page 2 -->
  <svg class="banner banner--full" style="top:720px" viewBox="0 0 1157 145" preserveAspectRatio="none">
    <rect width="1157" height="145" fill="url(#night-band)"/>
    <polygon points="0,0 355,0 285,72 430,145 0,145" fill="var(--white)"/>
    <polygon points="355,0 520,0 450,72 540,145 430,145 285,72" fill="var(--teal)"/>
    <polygon points="520,0 600,0 530,72 620,145 540,145 450,72" fill="var(--chevron)"/>
    <text class="logo-name" x="30" y="62">Halden</text>
    <text class="logo-name" x="30" y="118">Insurance</text>
    <text class="offer" x="350" y="38">Any Driver,</text>
    <text class="offer" x="430" y="82">Any Car,</text>
    <text class="offer" x="508" y="128">No Forms</text>
    <text class="premium" x="588" y="80">&amp; One Flat Premium*</text>
    <text class="learn" x="753" y="130"><tspan class="cta-link">Click Here</tspan> to Learn More</text>
    <circle cx="1095" cy="58" r="72" fill="url(#knob-tone)" role="img" aria-label="Photo of a chrome gear knob with shift pattern"/>
    <rect class="frame" x="1.5" y="1.5" width="1154" height="142"/>
  </svg>

  <!-- Full banner, page 2 mirrored -->
  <svg class="banner banner--full" style="top:798px" viewBox="0 0 1157 145" preserveAspectRatio="none">
    <rect width="1157" height="145" fill="url(#night-band)"/>
    <polygon points="1157,0 822,0 892,72 757,145 1157,145" fill="var(--white)"/>
    <polygon points="822,0 667,0 737,72 647,145 757,145 892,72" fill="var(--teal)"/>
    <polygon points="667,0 587,0 657,72 567,145 647,145 737,72" fill="var(--chevron)"/>
    <text class="logo-name" x="895" y="62">Halden</text>
    <text class="logo-name" x="895" y="118">Insurance</text>
    <circle cx="68" cy="72" r="72" fill="url(#knob-tone)" role="img" aria-label="Photo of a chrome gear knob with shift pattern"/>
    <text class="offer" x="155" y="38">Any Driver,</text>
    <text class="offer" x="233" y="82">Any Car,</text>
    <text class="offer" x="312" y="128">No Forms</text>
    <text class="premium" x="412" y="68">&amp; One Flat Premium*</text>
    <text class="learn" x="552" y="128"><tspan class="cta-link">Click Here</tspan> to Learn More</text>
    <rect class="frame" x="1.5" y="1.5" width="1154" height="142"/>
  </svg>

</main>
</body>
</html>
```